Web Design for Cedarfield Yard Crew

Cedarfield Yard Crew needs the photoshop files for a simple, clean and professional web design. I need a home and subpage design, although they can be very similar. See pagestridelab.com for a desired layout, although I'd like to see more design than shown on that site. The goal of the site is to attract both lawn maintenance/landscape customers and build a partner network of consultants that serve the US market. The following are needed:

- home and subpage design
- page: Home, Services, Locations, Consultants, FAQ, Contact
- if subpages have header photo, need to include 5 different header photos for each page
- favicon
Updates

I'll award the design based on the homepage concept. The minor subpage changes and other elements can be worked out in the workroom stage. Thanks, Reid

Industry/Entity Type

It Professional

```html
<!DOCTYPE html>
<html lang="en">
<head>
<meta charset="utf-8">
<title>Cedarfield Yard Crew</title>
<link rel="stylesheet" href="https://fonts.googleapis.com/css2?family=Open+Sans:ital,wght@0,400;0,600;0,700;1,400&display=swap">
<style>
:root{
  --green:#69b04f;
  --green-line:#8cc878;
  --nav:#56687f;
  --ink:#2b2b2b;
  --page:#fafafa;
  --band:#eef1f2;
  --field:#ebebeb;
  --footer:#5f6062;
  --overlay:rgba(95,95,95,.82);
  --white:#ffffff;
}
*{box-sizing:border-box;margin:0;padding:0}
html,body{width:1200px;height:1086px;overflow:hidden}
body{position:relative;background:var(--page);font-family:"Open Sans",Arial,sans-serif;color:var(--ink)}
.site-header{position:absolute;left:0;top:0;width:1200px;height:155px}
.brand{position:absolute;left:169px;top:57px;display:flex;align-items:center;gap:12px}
.brand-mark{width:34px;height:34px;background:var(--green);border-radius:4px}
.brand-name{font-size:24px;font-weight:600;color:#6b6b6b;letter-spacing:.3px}
.main-nav{position:absolute;right:169px;top:65px;display:flex;gap:28px}
.main-nav a{font-size:18px;font-weight:600;color:var(--nav);text-decoration:none}
.hero{position:absolute;left:0;top:155px;width:1200px;height:389px;
  background:linear-gradient(90deg,#8aa070 0%,#9db880 25%,#b7a98f 50%,#d9b49a 65%,#8fc7b8 85%,#6c8f55 100%);
  border-bottom:2px solid #b9cfe0}
.hero-card{position:absolute;left:171px;top:57px;width:377px;height:268px;background:var(--overlay);padding:20px 22px}
.hero-card h1{font-size:34px;line-height:38px;font-weight:700;color:var(--green)}
.hero-card p{margin-top:9px;font-size:18px;line-height:22.5px;color:var(--white)}
.content{position:absolute;left:0;top:544px;width:1200px;height:435px;background:linear-gradient(180deg,var(--band),var(--page) 60%)}
.intro{position:absolute;left:169px;top:38px;width:466px}
.intro h2{font-size:36px;font-weight:600;color:var(--green);line-height:48px}
.intro p{margin-top:20px;font-size:13px;line-height:17px;color:var(--ink)}
.intro p+p{margin-top:17px}
.signup{position:absolute;left:719px;top:38px;width:312px}
.signup h3{text-align:center;font-size:24px;line-height:29px;font-weight:600;color:var(--green)}
.signup-form{position:absolute;left:0;top:74px;width:312px;height:288px;border:1.5px solid var(--green-line);border-radius:12px;background:var(--page)}
.field{position:absolute;left:13px;width:284px;height:35px;background:var(--field);border-radius:3px;font-size:13.5px;font-style:italic;color:var(--green);padding:9px 12px}
.captcha{position:absolute;left:14px;top:160px;width:149px;height:33px;background:#666;color:var(--white);font-weight:700;font-size:19px;letter-spacing:11px;padding:2px 9px;font-family:"Courier New",monospace}
.submit{position:absolute;left:14px;top:249px;width:83px;height:20px;background:var(--green);border-radius:3px;color:var(--white);font-size:12px;font-weight:700;text-align:center;line-height:20px}
.site-footer{position:absolute;left:0;top:979px;width:1200px;height:107px;background:var(--footer);color:var(--white)}
.footer-nav{position:absolute;left:168px;top:21px;display:flex;gap:14px}
.footer-nav a{color:var(--white);text-decoration:none;font-size:14px}
.footer-meta{position:absolute;right:170px;top:21px;text-align:right;font-size:14px;line-height:23px}
</style>
</head>
<body>
<header class="site-header">
  <div class="brand"><span class="brand-mark"></span><span class="brand-name">Cedarfield Yard Crew</span></div>
  <nav class="main-nav">
    <a href="#">Home</a><a href="#">Services</a><a href="#">Locations</a><a href="#">Consultans</a><a href="#">FAQ</a><a href="#">Contact</a>
  </nav>
</header>

<section class="hero" role="img" aria-label="Family laughing together on a green front lawn before a house with flowering shrubs">
  <div class="hero-card">
    <h1>Orem ipsum dolor sit amet, consectet adipiscing elit.</h1>
    <p>Lorem ipsum dolor sit amet, consectetuer adipiscing elit. Maecenas porttitor congue massa. Fusce posuere, magna sed pulvinar ultricies, purus lectus malesuada libero, sit</p>
  </div>
</section>

<main class="content">
  <article class="intro">
    <h2>Orem ipsum dolor sit amet</h2>
    <p>Lorem ipsum dolor sit amet, consectetuer adipiscing elit. Maecenas porttitor congue massa. Fusce posuere, magna sed pulvinar ultricies, purus lectus male-suada libero, sit amet commodo magna eros quis urna. Nunc viverra imperdiet enim.</p>
    <p>Fusce est. Vivamus a tellus. Pellentesque habitant morbi tristique senectus et netus et malesuada fames ac turpis egestas. Proin pharetra nonummy pede. Mauris et orci. Aenean nec lorem. In porttitor. Donec laoreet nonummy augue. Suspendisse dui purus, scelerisque at, vulputate vitae, pretium mattis, nunc. Mauris eget neque at sem venenatis eleifend.</p>
  </article>
  <aside class="signup">
    <h3>Sign up to stay connected with Maple Hollow</h3>
    <div class="signup-form">
      <div class="field" style="top:17px">first name...</div>
      <div class="field" style="top:67px">last name...</div>
      <div class="field" style="top:117px">email address...</div>
      <div class="captcha">znqcez</div>
      <div class="field" style="top:201px">Enter word verification in box...</div>
      <div class="submit">submit</div>
    </div>
  </aside>
</main>

<footer class="site-footer">
  <nav class="footer-nav">
    <a href="#">home</a><a href="#">services</a><a href="#">locations</a><a href="#">consultans</a><a href="#">FAQ</a><a href="#">contact</a>
  </nav>
  <div class="footer-meta">@2014 maplehollow.co<br>start your page stride</div>
</footer>
</body>
</html>
```